Newsletter Design Project

I need a new design for a monthly newsletter that I do for Marbury Lane Open College Ipswich. I have been doing the same thing since 2009. We are based in Brisbane and we run classes for semi retired and retired people. I write about social activities, class activities, vacancies etc. I take photos and include them we hhave a logo that I always use. and would just like the newsletter to look different and fresh. The logo is Blue

```html
<!DOCTYPE html>
<html lang="en">
<head>
<meta charset="utf-8">
<title>Marbury Lane Open College Ipswich – Monthly Newsletter</title>
<link rel="stylesheet" href="https://fonts.googleapis.com/css2?family=Tinos:wght@400;700&display=swap">
<style>
  :root {
    --sky-light: #c4e4f5;
    --sky-mid: #3aa6dc;
    --sky-deep: #0a78bd;
    --panel: #ffffff;
    --ink: #111111;
    --rule: #1a1a1a;
    --photo-warm: #e9e2da;
    --photo-cool: #dfe7ef;
  }
  * { margin: 0; padding: 0; box-sizing: border-box; }
  html, body { width: 848px; height: 1200px; overflow: hidden; }
  body {
    position: relative;
    font-family: "Tinos", "Times New Roman", serif;
    color: var(--ink);
    background:
      radial-gradient(ellipse 520px 380px at 82% 6%, rgba(255,255,255,0.55), transparent 70%),
      radial-gradient(ellipse 460px 360px at 12% 48%, rgba(255,255,255,0.18), transparent 70%),
      linear-gradient(180deg, var(--sky-light) 0%, var(--sky-mid) 30%, #1f93d2 60%, var(--sky-deep) 100%);
  }
  .section-title {
    position: absolute;
    background: var(--panel);
    border-top: 1.5px solid var(--rule);
    border-bottom: 1.5px solid var(--rule);
    display: flex;
    align-items: center;
    justify-content: center;
    font-weight: 700;
    font-size: 28px;
    letter-spacing: 0.3px;
  }
  .section-body {
    position: absolute;
    background: var(--panel);
    padding: 5px 11px 0;
    overflow: hidden;
  }
  .section-body p {
    font-size: 15px;
    line-height: 22.4px;
    text-align: justify;
  }
  .photo {
    position: absolute;
    background: linear-gradient(160deg, #ffffff 0%, var(--photo-warm) 60%, #f6f3ef 100%);
  }
  .photo--reader {
    background: linear-gradient(160deg, #ffffff 0%, var(--photo-cool) 60%, #f4f6f8 100%);
  }
</style>
</head>
<body>
  <main class="newsletter">
    <article class="story story--intro">
      <h2 class="section-title" style="left:53px;top:52px;width:374px;height:59px;">LOREM IPSUM</h2>
      <div class="section-body" style="left:53px;top:122px;width:374px;height:178px;">
        <p>Lorem ipsum dolor sit amet, consectetur adipiscing elit. Aliquam semper metus id blandit posuere. Duis sem urna, vulputate et aliquam feugiat, sagittis nec tortor. Nunc erat diam, pharetra nec est ac, faucibus adipiscing ligula. Quisque vulputate nulla nisi. Aenean elit elit, luctus sit amet leo vitae, aliquam venenatis est. Mauris sollicitudin non eros vel aliquam.</p>
      </div>
      <div class="photo" role="img" aria-label="Photo of a smiling woman giving two thumbs up" style="left:448px;top:52px;width:352px;height:248px;"></div>
    </article>

    <article class="story story--wide">
      <h2 class="section-title" style="left:53px;top:330px;width:745px;height:63px;">LOREM IPSUM</h2>
      <div class="section-body" style="left:53px;top:404px;width:745px;height:195px;">
        <p>Lorem ipsum dolor sit amet, consectetur adipiscing elit. Aliquam semper metus id blandit posuere. Duis sem urna, vulputate et aliquam feugiat, sagittis nec tortor. Nunc erat diam, pharetra nec est ac, faucibus adipiscing ligula. Quisque vulputate nulla nisi. Aenean elit elit, luctus sit amet leo vitae, aliquam venenatis est. Mauris sollicitudin non eros vel aliquam. Phasellus rutrum mi nec risus imperdiet viverra. Morbi ut mauris quis metus ornare aliquam. Aenean metus risus, tincidunt sed tellus vel, ullamcorper gravida mi. Suspendisse ultrices erat id ipsum laoreet, eget luctus erat eleifend. Sed ac ipsum ligula. Sed volutpat sapien sit amet tellus condimentum, sed porttitor leo sollicitudin. Suspendisse porta lorem massa, non faucibus erat ultricies sit amet. Nullam ac libero id ipsum elementum aliquam. Praesent diam lorem, dictum at.</p>
      </div>
    </article>

    <article class="story story--feature">
      <div class="photo photo--reader" role="img" aria-label="Photo of an older man lying on the floor using a laptop" style="left:53px;top:629px;width:227px;height:218px;"></div>
      <h2 class="section-title" style="left:301px;top:629px;width:497px;height:52px;">LOREM IPSUM</h2>
      <div class="section-body" style="left:301px;top:691px;width:497px;height:156px;">
        <p>Lorem ipsum dolor sit amet, consectetur adipiscing elit. Aliquam semper metus id blandit posuere. Duis sem urna, vulputate et aliquam feugiat, sagittis nec tortor. Nunc erat diam, pharetra nec est ac, faucibus adipiscing ligula. Quisque vulputate nulla nisi. Aenean elit elit, luctus sit amet leo vitae, aliquam venenatis est. Mauris sollicitudin non eros vel aliquam. Phasellus rutrum mi nec risus imperdiet viverra morbi.</p>
      </div>
    </article>

    <article class="story story--wide">
      <h2 class="section-title" style="left:53px;top:871px;width:745px;height:65px;">LOREM IPSUM</h2>
      <div class="section-body" style="left:53px;top:949px;width:745px;height:199px;">
        <p>Lorem ipsum dolor sit amet, consectetur adipiscing elit. Aliquam semper metus id blandit posuere. Duis sem urna, vulputate et aliquam feugiat, sagittis nec tortor. Nunc erat diam, pharetra nec est ac, faucibus adipiscing ligula. Quisque vulputate nulla nisi. Aenean elit elit, luctus sit amet leo vitae, aliquam venenatis est. Mauris sollicitudin non eros vel aliquam. Phasellus rutrum mi nec risus imperdiet viverra. Morbi ut mauris quis metus ornare aliquam. Aenean metus risus, tincidunt sed tellus vel, ullamcorper gravida mi. Suspendisse ultrices erat id ipsum laoreet, eget luctus erat eleifend. Sed ac ipsum ligula. Sed volutpat sapien sit amet tellus condimentum, sed porttitor leo sollicitudin. Suspendisse porta lorem massa, non faucibus erat ultricies sit amet. Nullam ac libero id ipsum elementum aliquam. Praesent diam lorem, dictum at.</p>
      </div>
    </article>
  </main>
</body>
</html>
```